Electric mountain bike tours nz

We are an Electric Mountain bike tour company in New Zealand. We will be offering bike rental and guided tours around the Nelson region in New Zealand. I want our website to represent both Mountain biking and New Zealand with the colours layout and features. We want tabs for the following:
-1 about us
-2 what we offer
-3 bookings/contact
Under the about us tab will be who we are as a a company. I want the ability to add videos to each of these tabs as we move foward with videos of the tracks we will be riding. I want the website to be editable so I can add and remove videos/photos myself. Also "our bikes" will be under this tab.
Under the what we offer tab will be
-1 bike rental and pricing
-2 guided tours and pricing
-3 recommended package deals.
I want to able to put the tracks under the guided tours tab and select beginner/ intermediate/advanced and have the tracks in each of the following to match the rider level. Also to be able to have a small video of the track would be great in this section.
Bookings and contact tab
(Further information for this tab to be updated soon)
- Silver ferns, kiwi, mountains

```html
<!DOCTYPE html>
<html lang="en">
<head>
<meta charset="utf-8">
<title>Wheels — E-MTB Rentals &amp; Guided Tours, Nelson NZ</title>
<link href="https://fonts.googleapis.com/css2?family=Raleway:wght@400;500;600;700;800&family=Open+Sans:wght@400;600&display=swap" rel="stylesheet">
<style>
  :root {
    --ink: #1c1c1c;
    --muted: #777;
    --white: #ffffff;
    --navy: #1f2a4a;
    --fern: #2f8a5a;
    --fern-dark: #1f6b44;
    --line: #ececec;
    --photo-bg: #f4f4f4;
  }
  * { box-sizing: border-box; margin: 0; padding: 0; }
  html, body { width: 714px; height: 1200px; overflow: hidden; background: var(--white); }
  body { font-family: "Raleway", sans-serif; color: var(--ink); }

  .hero { position: relative; height: 360px; overflow: hidden; }
  .hero-photo {
    position: absolute; inset: 0;
    background:
      radial-gradient(ellipse at 60% 50%, rgba(170,60,40,.45) 0%, transparent 45%),
      radial-gradient(ellipse at 30% 85%, rgba(150,120,50,.55) 0%, transparent 55%),
      linear-gradient(180deg, #0d1730 0%, #1d2a22 35%, #2f3a20 70%, #3a3218 100%);
  }
  .hero-shade { position: absolute; inset: 0; background: rgba(0,0,0,.25); }
  .brand {
    position: absolute; left: 36px; top: 18px;
    display: flex; align-items: center; gap: 8px;
    color: var(--white); font-weight: 800; font-size: 15px; letter-spacing: 1px;
  }
  .brand-dot { width: 22px; height: 22px; border-radius: 50%; background: var(--white); }
  .menu {
    position: absolute; right: 48px; top: 38px; color: var(--white);
    font-size: 10px; font-weight: 700; letter-spacing: 1.5px; display: flex; align-items: center; gap: 3px;
  }
  .hero-title { position: absolute; top: 150px; width: 100%; text-align: center; color: var(--white); }
  .hero-title h1 { font-size: 34px; font-weight: 600; letter-spacing: 4px; line-height: 1; }
  .hero-title p { font-size: 18px; font-weight: 600; letter-spacing: 3px; margin-top: 6px; }
  .search {
    position: absolute; top: 228px; left: 124px; width: 466px; height: 32px;
    display: flex; background: var(--white); font-size: 9px; font-weight: 600; letter-spacing: 1px;
  }
  .search-field { display: flex; align-items: center; gap: 10px; padding-left: 24px; width: 118px; }
  .search-field.city { width: 124px; justify-content: space-between; padding-right: 10px; }
  .ride-now {
    margin-left: auto; width: 116px; background: var(--navy); color: var(--white);
    font-size: 15px; font-weight: 500; display: flex; align-items: center; justify-content: center; letter-spacing: .5px;
  }
  .scroll-hint { position: absolute; left: 350px; top: 325px; }

  .site-nav {
    height: 32px; display: flex; align-items: center; padding: 0 70px;
    box-shadow: 0 3px 6px rgba(0,0,0,.12); position: relative;
  }
  .site-nav .logo-word { font-weight: 800; font-size: 11px; letter-spacing: 1.5px; }
  .site-nav ul { list-style: none; display: flex; gap: 36px; margin-left: auto; font-size: 6.5px; font-weight: 600; letter-spacing: 1px; }

  .about { text-align: center; padding: 16px 100px 0; height: 108px; }
  .section-title { font-weight: 800; font-size: 11px; letter-spacing: 2px; }
  .section-sub { font-size: 6.5px; color: var(--muted); letter-spacing: .5px; margin-top: 2px; }
  .about svg { margin: 5px 0 3px; }
  .about-text { font-family: "Open Sans", sans-serif; font-size: 5.5px; line-height: 1.6; color: var(--muted); text-align: justify; }

  .stats { position: relative; height: 168px; margin-top: 8px; color: var(--white); text-align: center; overflow: hidden; }
  .stats-photo {
    position: absolute; inset: 0;
    background: linear-gradient(90deg, #3a3228 0%, #4a4a2a 25%, #2b3440 55%, #3b4a40 80%, #2a2a2a 100%);
  }
  .stats-shade { position: absolute; inset: 0; background: rgba(0,0,0,.45); }
  .stats-inner { position: relative; padding-top: 32px; }
  .stats h2 { font-size: 11px; font-weight: 700; letter-spacing: 2px; }
  .stats .lead { font-family: "Open Sans", sans-serif; font-size: 6px; opacity: .85; margin-top: 2px; }
  .stat-row { display: flex; justify-content: center; gap: 70px; margin-top: 20px; }
  .stat { width: 90px; }
  .stat-num { font-size: 27px; font-weight: 600; letter-spacing: 3px; line-height: 1; }
  .stat-label { font-size: 8px; font-weight: 500; margin-top: 4px; line-height: 1.25; }

  .fleet { text-align: center; padding-top: 12px; height: 392px; }
  .fleet .section-title { font-size: 14px; letter-spacing: 2.5px; }
  .fleet .section-sub { color: var(--ink); font-size: 6.5px; }
  .bike-grid { display: grid; grid-template-columns: repeat(3, 160px); justify-content: center; column-gap: 17px; row-gap: 14px; margin-top: 12px; }
  .bike-photo { height: 92px; }
  .bike-photo.dark { background: linear-gradient(180deg, var(--white) 0%, #d8d8d8 50%, var(--white) 100%); }
  .bike-photo.green { background: linear-gradient(180deg, var(--white) 0%, #c8eeb4 50%, var(--white) 100%); }
  .bike-photo.silver { background: linear-gradient(180deg, var(--white) 0%, #e2e2e2 50%, var(--white) 100%); }
  .bike-name { font-size: 9px; font-weight: 700; letter-spacing: 1.5px; margin-top: 10px; }
  .bike-price { font-size: 12px; font-weight: 500; letter-spacing: .5px; }
  .bike-link { font-size: 6.5px; font-weight: 600; letter-spacing: .8px; text-decoration: underline; margin-top: 2px; }

  .offers { text-align: center; }
  .offers .section-title { font-size: 15px; letter-spacing: 2.5px; }
  .offer-grid { display: grid; grid-template-columns: repeat(2, 230px); justify-content: center; gap: 12px 20px; margin-top: 16px; text-align: left; }
  .offer-card { height: 78px; border: 1px solid var(--line); box-shadow: 0 1px 4px rgba(0,0,0,.05); display: flex; gap: 18px; padding: 18px 14px; }
  .offer-icon { width: 44px; height: 36px; border-radius: 6px; background: linear-gradient(135deg, var(--fern), var(--fern-dark)); flex: none; }
  .offer-card h3 { font-family: "Open Sans", sans-serif; font-size: 7.5px; font-weight: 600; }
  .offer-card p { font-family: "Open Sans", sans-serif; font-size: 6px; line-height: 1.5; color: #555; margin-top: 5px; }
</style>
</head>
<body>
  <header class="hero">
    <div class="hero-photo" role="img" aria-label="Electric mountain bike parked on a grassy Nelson hill trail at dusk"></div>
    <div class="hero-shade"></div>
    <div class="brand"><span class="brand-dot"></span>KEAWHEEL</div>
    <div class="menu">MENU
      <svg width="9" height="8" viewBox="0 0 9 8"><path d="M0 1h9M0 4h9M0 7h9" stroke="#fff" stroke-width="1.4"/></svg>
    </div>
    <div class="hero-title">
      <h1>SELF RIDE BIKE RENTALS</h1>
      <p>NOW STARTS @ NZ$8/HOUR*</p>
    </div>
    <form class="search">
      <div class="search-field city">NELSON
        <svg width="8" height="5" viewBox="0 0 8 5"><path d="M0 0h8L4 5z" fill="#1f2a4a"/></svg>
      </div>
      <div class="search-field">START TRIP
        <svg width="16" height="16" viewBox="0 0 16 16" fill="none" stroke="#1f2a4a" stroke-width="1"><rect x="1" y="3" width="12" height="11"/><path d="M1 6h12M4 1v3M10 1v3"/><circle cx="12" cy="12" r="3" fill="#fff"/></svg>
      </div>
      <div class="search-field">END TRIP
        <svg width="16" height="16" viewBox="0 0 16 16" fill="none" stroke="#1f2a4a" stroke-width="1"><rect x="1" y="3" width="12" height="11"/><path d="M1 6h12M4 1v3M10 1v3"/><circle cx="12" cy="12" r="3" fill="#fff"/></svg>
      </div>
      <div class="ride-now">RIDE NOW</div>
    </form>
    <svg class="scroll-hint" width="14" height="22" viewBox="0 0 14 22" fill="none" stroke="#fff" stroke-width="1"><rect x="1" y="1" width="12" height="20" rx="6"/><path d="M7 5v4"/></svg>
  </header>

  <nav class="site-nav">
    <span class="logo-word">WHEELS</span>
    <ul><li>HOME</li><li>ABOUT US</li><li>WHAT WE OFFER</li><li>BOOKINGS/CONTACT</li><li>BLOG</li></ul>
  </nav>

  <section class="about">
    <h2 class="section-title">ABOUT US</h2>
    <p class="section-sub">Let's talk about what makes your company great.</p>
    <svg width="32" height="18" viewBox="0 0 32 18" fill="none" stroke="#1c1c1c" stroke-width="1.4"><circle cx="7" cy="11" r="6"/><circle cx="25" cy="11" r="6"/><path d="M7 11l6-7h8l4 7M13 4l4 7h-10M20 2h3"/></svg>
    <p class="about-text">We are a small team of riders based in Nelson, New Zealand, sharing the trails we love on quality electric mountain bikes. Whether you want to explore on your own or join one of our local guides, we match every ride to your level and pace. From native bush singletrack and fern-lined valleys to big mountain views over Tasman Bay, our tours show off the best of the region. Every bike is serviced after each hire, every guide knows the tracks by heart, and every booking comes with local tips, safety gear and a warm kiwi welcome. Come ride with us and see Nelson the way we do, one trail at a time.</p>
  </section>

  <section class="stats">
    <div class="stats-photo" role="img" aria-label="Row of mountain bikes parked in front of a painted wall"></div>
    <div class="stats-shade"></div>
    <div class="stats-inner">
      <h2>SOME STATISTICS</h2>
      <p class="lead">A few numbers from our years on the Nelson trails, guiding riders of every level across the region.</p>
      <div class="stat-row">
        <div class="stat"><div class="stat-num">409</div><div class="stat-label">BIKES RENTED</div></div>
        <div class="stat"><div class="stat-num">2012</div><div class="stat-label">YEAR THE<br>COMPANY STARTED</div></div>
        <div class="stat"><div class="stat-num">0</div><div class="stat-label">UNSATISFIED<br>CUSTOMERS</div></div>
      </div>
    </div>
  </section>

  <section class="fleet">
    <h2 class="section-title">OUR BRAND IS OUR FLEET</h2>
    <p class="section-sub">Your chance to shine</p>
    <div class="bike-grid">
      <article><div class="bike-photo dark" role="img" aria-label="Black electric mountain bike"></div><h3 class="bike-name">ORANGEZ</h3><p class="bike-price">$399</p><p class="bike-link">Learn more</p></article>
      <article><div class="bike-photo green" role="img" aria-label="Green single-speed bike"></div><h3 class="bike-name">GREEN DEVIL</h3><p class="bike-price">$399</p><p class="bike-link">Learn more</p></article>
      <article><div class="bike-photo silver" role="img" aria-label="Silver and black electric mountain bike"></div><h3 class="bike-name">BLUE LAGOON</h3><p class="bike-price">$399</p><p class="bike-link">Learn more</p></article>
      <article><div class="bike-photo dark" role="img" aria-label="Black electric mountain bike"></div><h3 class="bike-name">ORANGEZ</h3><p class="bike-price">$399</p><p class="bike-link">Learn more</p></article>
      <article><div class="bike-photo green" role="img" aria-label="Green single-speed bike"></div><h3 class="bike-name">GREEN DEVIL</h3><p class="bike-price">$399</p><p class="bike-link">Learn more</p></article>
      <article><div class="bike-photo silver" role="img" aria-label="Silver and black electric mountain bike"></div><h3 class="bike-name">BLUE LAGOON</h3><p class="bike-price">$399</p><p class="bike-link">Learn more</p></article>
    </div>
  </section>

  <section class="offers">
    <h2 class="section-title">WHAT WE OFFER?</h2>
    <div class="offer-grid">
      <div class="offer-card"><div class="offer-icon" role="img" aria-label="Fern green bike rental badge"></div><div><h3>Bike Rental &amp; Pricing</h3><p>Electric mountain bikes assured by Trailhouse, hired by the hour or day across Nelson.</p></div></div>
      <div class="offer-card"><div class="offer-icon" role="img" aria-label="Fern green guided tour badge"></div><div><h3>Guided Tours</h3><p>Beginner, intermediate and advanced Nelson tracks, each matched to your riding level.</p></div></div>
      <div class="offer-card"><div class="offer-icon" role="img" aria-label="Fern green package badge"></div><div><h3>Package Deals</h3><p>Bundle a rental with a guided tour and save on your ride through the Nelson region.</p></div></div>
      <div class="offer-card"><div class="offer-icon" role="img" aria-label="Fern green price badge"></div><div><h3>Lowest Price Guarantee</h3><p>Get all your favourite bikes for rent at the lowest possible price on the bike rental market.</p></div></div>
    </div>
  </section>
</body>
</html>
```